Flyer-Design für Kindertagesstätte
Helmsteds Kinderhafen suchte ein neues Design in der Kategorie Flyer und hat ein Projekt auf grafikfinden.de gestartet.
Zielgruppe
Wir sind eine Kindertagesstätte und wollen eine Baby-Kind-Spielgruppe jeden Mittwoch in unserer Kita von 09.00 Uhr bis 11.00 Uhr anbieten.
Aufgabenstellung
Unser LOGO muss im Flyer enthalten sein, auf jeden Fall ein Bild wenn möglich mit mehreren Babys/Kleinkindern bis 1,5 Jahre. Wir benötigen den Flyer in DIN lang - bunt - 1 seitig.
Folgender Text sollte enthalten: Baby-Kind-Spielgruppe, jeden mittwoch in unserer Kita 'Helmsteds Kinderhafen' von 09.00 Uhr bis 11.00 Uhr. Die Spielgruppe wird durch unser ausgebildetes Fachpersonal begleitet.

```html
<!DOCTYPE html>
<html lang="de">
<head>
<meta charset="utf-8">
<title>Baby-Kind Spielgruppe – Flyer</title>
<link rel="stylesheet" href="https://fonts.googleapis.com/css2?family=Baloo+2:wght@600;700&family=Comfortaa:wght@600;700&family=Roboto+Slab:wght@800&display=swap">
<style>
  :root {
    --orange: #e2520f;
    --orange-deep: #c9440a;
    --white: #ffffff;
    --page: #f1f0ee;
    --green: #8cbc1e;
    --blue: #2fb1e3;
    --ochre: #d6a312;
    --pink: #e2409a;
    --block-orange: #e4561a;
  }
  * { box-sizing: border-box; margin: 0; padding: 0; }
  html, body { width: 686px; height: 1200px; overflow: hidden; background: var(--page); }
  .flyer {
    position: absolute; left: 67px; top: 10px; width: 552px; height: 1180px;
    background: var(--orange); overflow: hidden;
    box-shadow: 0 6px 22px rgba(0,0,0,.12);
    font-family: "Comfortaa", "Quicksand", sans-serif;
  }
  .photo { position: absolute; }
  .photo--top {
    left: 0; top: 36px; width: 552px; height: 420px;
    background: linear-gradient(160deg, #e9d6c3 0%, #f4c9a8 35%, #f2b7b9 60%, #b9c7d8 100%);
  }
  .photo--baby {
    left: 318px; top: 745px; width: 234px; height: 390px;
    border-radius: 110px 60px 30px 40px;
    background: linear-gradient(170deg, #f2cdb5 0%, #e07ac8 45%, #b445b8 80%, #8a4cc0 100%);
  }
  .shapes { position: absolute; inset: 0; }
  .logo {
    position: absolute; left: 200px; top: 22px; width: 180px;
    text-align: center; color: var(--orange);
  }
  .logo__dot { width: 58px; height: 58px; border-radius: 50%; background: var(--orange); margin: 0 auto 12px; }
  .logo__name { font-weight: 700; font-size: 17px; line-height: 1.2; }
  .blocks { position: absolute; left: 0; top: 0; }
  .block {
    position: absolute; width: 112px; height: 112px; border-radius: 14px;
    display: flex; align-items: center; justify-content: center;
    font-family: "Roboto Slab", "Rockwell", serif; font-weight: 800; font-size: 88px;
    color: var(--white); line-height: 1;
    box-shadow: inset 0 0 0 6px rgba(0,0,0,.13);
  }
  .block--orange { background: var(--block-orange); }
  .block--green { background: var(--green); }
  .block--blue { background: var(--blue); }
  .block--ochre { background: var(--ochre); }
  .block--pink { background: var(--pink); }
  .hyphen { position: absolute; left: 198px; top: 550px; width: 30px; height: 8px; background: var(--ochre); border-radius: 2px; }
  .subtitle {
    position: absolute; left: 0; width: 552px; top: 698px; text-align: center;
    font-family: "Baloo 2", sans-serif; font-weight: 700; font-size: 40px; color: var(--orange);
  }
  .facts { position: absolute; left: 36px; top: 822px; width: 300px; list-style: none; color: var(--white); }
  .fact { display: flex; align-items: flex-start; gap: 16px; font-size: 18px; font-weight: 700; line-height: 1.3; letter-spacing: .3px; margin-bottom: 24px; }
  .fact svg { flex: none; width: 42px; height: 42px; }
  .contact { position: absolute; left: 38px; top: 1050px; list-style: none; color: var(--white); font-size: 11px; font-weight: 600; line-height: 22px; }
  .contact svg { width: 10px; height: 10px; vertical-align: -1px; margin-right: 4px; }
  .web {
    position: absolute; left: 0; width: 552px; top: 1140px; text-align: center;
    color: var(--orange); font-weight: 700; font-size: 20px;
  }
</style>
</head>
<body>
<main class="flyer">
  <div class="photo photo--top" role="img" aria-label="Foto: zwei Kleinkinder spielen mit einem bunten Holz-Steckspiel"></div>
  <div class="photo photo--baby" role="img" aria-label="Foto: Baby im pinken Kleid mit Stapelbechern A B C"></div>

  <svg class="shapes" viewBox="0 0 552 1180" aria-hidden="true">
    <g fill="#ffffff">
      <!-- logo cloud -->
      <rect x="210" y="0" width="160" height="90"/>
      <circle cx="235" cy="85" r="55"/>
      <circle cx="345" cy="85" r="55"/>
      <circle cx="290" cy="120" r="60"/>
      <!-- title cloud -->
      <rect x="0" y="470" width="552" height="240"/>
      <circle cx="80" cy="500" r="80"/>
      <circle cx="200" cy="465" r="80"/>
      <circle cx="330" cy="455" r="78"/>
      <circle cx="460" cy="480" r="82"/>
      <circle cx="60" cy="700" r="60"/>
      <circle cx="170" cy="725" r="65"/>
      <circle cx="285" cy="745" r="70"/>
      <circle cx="400" cy="720" r="65"/>
      <circle cx="510" cy="690" r="55"/>
      <!-- bottom band -->
      <path d="M0 1150 Q276 1100 552 1120 L552 1180 L0 1180 Z"/>
    </g>
  </svg>

  <div class="logo">
    <div class="logo__dot"></div>
    <div class="logo__name">Helmsteds Kinderhafen</div>
  </div>

  <h1 class="blocks" aria-label="Baby-Kind">
    <span class="block block--orange" style="left:34px;top:440px;transform:rotate(-4deg)">B</span>
    <span class="block block--green" style="left:157px;top:424px;transform:rotate(2deg)">A</span>
    <span class="block block--blue" style="left:282px;top:420px;transform:rotate(-3deg)">B</span>
    <span class="block block--ochre" style="left:410px;top:420px;transform:rotate(3deg)">Y</span>
    <span class="hyphen"></span>
    <span class="block block--ochre" style="left:30px;top:572px;transform:rotate(-5deg)">K</span>
    <span class="block block--pink" style="left:155px;top:570px;transform:rotate(3deg)">I</span>
    <span class="block block--orange" style="left:280px;top:565px;transform:rotate(-3deg)">N</span>
    <span class="block block--green" style="left:408px;top:555px;transform:rotate(4deg)">D</span>
  </h1>
  <p class="subtitle">Spielgruppe</p>

  <ul class="facts">
    <li class="fact">
      <svg viewBox="0 0 42 42" fill="none" stroke="#fff" stroke-width="2.2" stroke-linecap="round" stroke-linejoin="round"><rect x="4" y="8" width="34" height="30" rx="4"/><path d="M4 16h34M13 4v8M29 4v8"/><path d="M21 33c-5-3.5-7-5.5-7-8a3.5 3.5 0 0 1 7-1 3.5 3.5 0 0 1 7 1c0 2.5-2 4.5-7 8z"/></svg>
      <span>Mittwochs 09.00 Uhr<br>- 11.00 Uhr in der Kita</span>
    </li>
    <li class="fact">
      <svg viewBox="0 0 42 42" fill="none" stroke="#fff" stroke-width="2.2" stroke-linecap="round" stroke-linejoin="round"><path d="M21 24c-7-5-10-8-10-12a5 5 0 0 1 10-1.5 5 5 0 0 1 10 1.5c0 4-3 7-10 12z"/><path d="M5 14v12l8 10M37 14v12l-8 10"/></svg>
      <span>begleitet von unserem ausgebildeten Fach-<br>personal</span>
    </li>
    <li class="fact">
      <svg viewBox="0 0 42 42" fill="none" stroke="#fff" stroke-width="2.2" stroke-linecap="round"><circle cx="21" cy="22" r="15"/><path d="M18 7c0-3 5-3 5 0"/></svg>
      <span>für Kinder von 6 bis 18<br>Monate</span>
    </li>
  </ul>

  <ul class="contact">
    <li><svg viewBox="0 0 10 10" fill="none" stroke="#fff" stroke-width="1"><path d="M5 9.5S1.5 6 1.5 4a3.5 3.5 0 0 1 7 0C8.5 6 5 9.5 5 9.5z"/><circle cx="5" cy="4" r="1.2"/></svg>Lindenweg 14 | 04109 Leipzig</li>
    <li><svg viewBox="0 0 10 10" fill="none" stroke="#fff" stroke-width="1"><path d="M2 1l2 2-1 1.5a6 6 0 0 0 2.5 2.5L7 6l2 2-1.5 1.5C4 9 1 6 .5 2.5z"/></svg>Telefon: 0341 - 2207 415</li>
    <li><svg viewBox="0 0 10 10" fill="none" stroke="#fff" stroke-width="1"><rect x=".5" y="2" width="9" height="6"/><path d="M.5 2L5 5.5 9.5 2"/></svg>info@helmsteds-kinderhafen.de</li>
  </ul>

  <p class="web">www.helmsteds-kinderhafen.de</p>
</main>
</body>
</html>
```